2022 Grenache Hillside Vineyard Sketch Wine Label

Size:4"X4"
Wine: 2022 Grenache
Vineyard Name: Low Mill Vineyard
AVA: Solano County
Alcohol by Volume:15%
Volume:750ml
Must Feature a hillside vineyard on the label somehow, I picture it being a sketch but it doesn't have to be. Not looking for anything flashy or colorful but maybe a pop of color somewhere. I am not yet sure that I want to include our name, but you can try to work in "KMT" somewhere on the label if it fits the design.
The Label must include all the information listed above. The Grenache was grown in a hillside vineyard, so I wanted the label to prominently feature a hillside vineyard. You can layout the label however you see best, but the vintage and varietal should be prominent, the ABV can be in small type face but must be legible following FQD guidelines. If you are able to make the vineyard name pop as well that would be good.
You don't have to use these, but our standard fonts we use are:
For Varietal: Bianca
Secondary (vintage, AVA, Vineyard):Helvetica
ABV/Volume: PT Serif
Thank you, look forward to the results

```html
<!DOCTYPE html>
<html lang="en">
<head>
<meta charset="utf-8">
<title>2022 Grenache – Low Mill Vineyard Label</title>
<link href="https://fonts.googleapis.com/css2?family=IM+Fell+English&family=Smokum&family=Josefin+Sans:wght@400&display=swap" rel="stylesheet">
<style>
  :root {
    --page-bg: #d9d9d9;
    --paper: #f2f2f0;
    --ink: #141414;
    --wine-red: #c30f12;
    --sketch-light: #ecebe8;
    --sketch-mid: #bdbcb8;
    --sketch-dark: #6e6d6a;
  }
  * { margin: 0; padding: 0; box-sizing: border-box; }
  html, body {
    width: 1200px;
    height: 1040px;
    overflow: hidden;
    background: var(--page-bg);
  }
  .label {
    position: absolute;
    left: 100px;
    top: 20px;
    width: 1000px;
    height: 1000px;
    background: var(--paper);
    overflow: hidden;
  }
  .label__edge {
    position: absolute;
    left: 0;
    width: 100%;
    height: 33px;
    background: repeating-linear-gradient(
      to right,
      transparent 0 34.48px,
      var(--page-bg) 34.48px 68.97px
    );
  }
  .label__edge--top { top: 0; }
  .label__edge--bottom { bottom: 0; }
  .label__vintage {
    position: absolute;
    top: 104px;
    width: 100%;
    text-align: center;
    font-family: "IM Fell English", serif;
    font-size: 68px;
    letter-spacing: 0.12em;
    padding-left: 0.12em;
    color: var(--ink);
    line-height: 1;
  }
  .label__varietal {
    position: absolute;
    left: 0;
    top: 170px;
    width: 1000px;
    height: 140px;
  }
  .label__varietal text {
    font-family: "Smokum", serif;
    font-size: 170px;
    fill: var(--wine-red);
  }
  .label__scene {
    position: absolute;
    left: 20px;
    top: 323px;
    width: 967px;
    height: 417px;
    border-radius: 50% 50% 45% 45% / 30% 30% 60% 60%;
    background: radial-gradient(ellipse at 45% 55%, var(--sketch-dark) 0%, var(--sketch-mid) 45%, var(--sketch-light) 75%, var(--paper) 100%);
  }
  .label__vineyard {
    position: absolute;
    top: 766px;
    width: 100%;
    text-align: center;
    font-family: "IM Fell English", serif;
    font-size: 32px;
    letter-spacing: 0.2em;
    padding-left: 0.2em;
    color: var(--wine-red);
    line-height: 1;
    white-space: nowrap;
  }
  .label__facts {
    position: absolute;
    top: 882px;
    left: 62px;
    right: 69px;
    display: flex;
    justify-content: space-between;
    font-family: "Josefin Sans", sans-serif;
    font-size: 25px;
    letter-spacing: 0.04em;
    color: var(--ink);
    line-height: 1;
    white-space: nowrap;
  }
</style>
</head>
<body>
  <main class="label">
    <div class="label__edge label__edge--top"></div>
    <p class="label__vintage">2022</p>
    <h1 class="label__varietal">
      <svg width="1000" height="140" viewBox="0 0 1000 140" aria-label="Grenache">
        <text x="185" y="134" textLength="633" lengthAdjust="spacingAndGlyphs">GRENACHE</text>
      </svg>
    </h1>
    <div class="label__scene" role="img" aria-label="Pen-and-ink sketch of a hillside vineyard with rows of vines, a tractor, a farmhouse, trees, a fence and a winding path"></div>
    <p class="label__vineyard">LOW MILL VINEYARD</p>
    <div class="label__facts">
      <span class="label__abv">ABV: 15%</span>
      <span class="label__ava">AVA: SOLANO COUNTY</span>
      <span class="label__volume">750ML</span>
    </div>
    <div class="label__edge label__edge--bottom"></div>
  </main>
</body>
</html>
```